Merriwick Law - New Letterhead/Logo

Hello!
THE FIRM NAME IS NOW MERRIWICK LAW. We recently just changed our name and we are in need of a classy letterhead. Attached I have a logo we have included in the past, but we are willing to look at other alternatives as well. I will also attach our current letterhead with our old name, Merriwick Law. We are willing to go without attorney names. Please help! Thanks

```html
<!DOCTYPE html>
<html lang="en">
<head>
<meta charset="utf-8">
<title>Merriwick Law Letterhead</title>
<link href="https://fonts.googleapis.com/css2?family=Roboto+Condensed:wght@400&display=swap" rel="stylesheet">
<style>
  :root {
    --firm-green: #448f80;
    --watermark-tint: #eaf3f1;
    --footer-grey: #dcdcdc;
    --paper: #ffffff;
    --ink-light: #ffffff;
  }
  html, body {
    margin: 0;
    padding: 0;
    overflow: hidden;
    background: var(--paper);
  }
  .letterhead {
    position: relative;
    width: 923px;
    height: 1200px;
    overflow: hidden;
    background: var(--paper);
    font-family: "Roboto Condensed", "Arial Narrow", sans-serif;
  }
  .header-band,
  .footer-bands {
    position: absolute;
    left: 0;
    display: block;
  }
  .header-band { top: 0; }
  .footer-bands { bottom: 0; }
  .header-mark {
    position: absolute;
    left: 12px;
    top: 26px;
    width: 38px;
    height: 38px;
    background: var(--ink-light);
  }
  .firm-title {
    position: absolute;
    left: 69px;
    top: 31px;
    margin: 0;
    font-size: 27px;
    font-weight: 400;
    line-height: 1;
    color: var(--ink-light);
    letter-spacing: 0.2px;
    white-space: nowrap;
  }
  .title-rule {
    position: absolute;
    left: 72px;
    top: 72px;
    width: 484px;
    height: 1px;
    background: var(--ink-light);
  }
  .scales-emblem {
    position: absolute;
    left: 784px;
    top: 0;
    width: 139px;
    height: 98px;
    background: var(--firm-green);
    opacity: 0.85;
  }
  .scales-watermark {
    position: absolute;
    left: 0;
    top: 111px;
    width: 197px;
    height: 385px;
    background: linear-gradient(180deg, rgba(234,243,241,0.6), var(--watermark-tint));
  }
  .name-watermark {
    position: absolute;
    right: 10px;
    top: 880px;
    margin: 0;
    text-align: right;
    font-size: 76px;
    font-weight: 400;
    line-height: 1.1;
    color: var(--watermark-tint);
  }
</style>
</head>
<body>
  <div class="letterhead">
    <svg class="header-band" width="722" height="94" viewBox="0 0 722 94" aria-hidden="true">
      <polygon points="0,0 722,0 540,94 0,94" fill="var(--firm-green)"/>
    </svg>
    <span class="header-mark" aria-hidden="true"></span>
    <h1 class="firm-title">LAW OFFICES OF MERRIWICK LAW, LLC</h1>
    <span class="title-rule" aria-hidden="true"></span>

    <div class="scales-emblem" role="img" aria-label="Scales of justice emblem"></div>
    <div class="scales-watermark" role="img" aria-label="Faint scales of justice pan decoration"></div>

    <p class="name-watermark" aria-hidden="true">Merriwick<br>Law</p>

    <svg class="footer-bands" width="923" height="21" viewBox="0 0 923 21" aria-hidden="true">
      <polygon points="0,0 423,0 450,21 0,21" fill="var(--footer-grey)"/>
      <polygon points="446,0 923,0 923,21 472,21" fill="var(--firm-green)"/>
    </svg>
  </div>
</body>
</html>
```